Corvalo Bar

I have TWO premises that are currently construction sites, so I need a billboard/poster to say 'coming soon' - see http://www.corvalobar.example.nz/
(do not want dates to be included and unlike the picture on this site, must hide brand of beer - Brisca is not one of our beers)
Needs to say things like, but not limited to:-
‘TAPAS – The Art of Eating Standing Up – Coming Soon’
‘A Taste of Spain’
‘Largest Selection of Spanish Beers in the WORLD!’
‘Largest Selection of Spanish Wines in New Zealand!’
‘over 70 Spanish Beers’
‘over 50 Spanish Wines’
‘4 Draft Spanish Craft Beers’
‘Authentic Spanish Café/Deli/Tapas Bar’
'Tapas Menu created by Tomas Larrea Vidal'
'Freshly Roasted Torrefacto Coffee'
Must include Website URL - http://www.corvalobar.example.nz/
Needs to be visually outstanding, as premises on main road. I don't see this as a logo and a series of bullet points but a true piece of marketing genius. Incorporating the Spanish Flag somewhere is OK to add colour
Note Corvalo® and Corval® are Resigtered Trademarks in New Zealand
Logo's can be downloaded from http://www.corvalobar.example.nz/CorvaloLogos.zip
Intending to print on coreflute sheet 3050mm x 1500mm with Digital Printed Media applied to Coreflute

```html
<!DOCTYPE html>
<html lang="en">
<head>
<meta charset="utf-8">
<title>Corvalo Bar – Coming Soon</title>
<link rel="stylesheet" href="https://fonts.googleapis.com/css2?family=Oswald:wght@300;400&family=Pinyon+Script&display=swap">
<style>
  :root {
    --ink: #fbf7ef;
    --roast-dark: #3b2416;
    --roast-mid: #6a4429;
    --wood-light: #9c7a58;
  }
  html, body {
    margin: 0;
    padding: 0;
    width: 1200px;
    height: 593px;
    overflow: hidden;
    background: var(--roast-dark);
  }
  .billboard {
    position: relative;
    width: 1200px;
    height: 593px;
  }
  .billboard svg {
    display: block;
    width: 1200px;
    height: 593px;
  }
  .condensed {
    font-family: 'Oswald', 'Arial Narrow', sans-serif;
    font-weight: 300;
    fill: var(--ink);
  }
  .brand-name {
    font-weight: 400;
  }
  .script {
    font-family: 'Pinyon Script', cursive;
    fill: var(--ink);
  }
  .frame-line {
    fill: none;
    stroke: var(--ink);
    stroke-width: 3.5;
  }
  .icon {
    fill: var(--ink);
  }
  .icon-stroke {
    fill: none;
    stroke: var(--ink);
    stroke-width: 3;
    stroke-linecap: round;
  }
</style>
</head>
<body>
<main class="billboard">
  <svg viewBox="0 0 1200 593" xmlns="http://www.w3.org/2000/svg">
    <defs>
      <radialGradient id="beans-on-wood" cx="45%" cy="40%" r="80%">
        <stop offset="0" stop-color="var(--wood-light)"/>
        <stop offset="0.45" stop-color="var(--roast-mid)"/>
        <stop offset="1" stop-color="var(--roast-dark)"/>
      </radialGradient>
    </defs>

    <rect class="backdrop" x="0" y="0" width="1200" height="593" fill="url(#beans-on-wood)"
          role="img" aria-label="Photograph of roasted coffee beans and a scoop of ground coffee scattered on weathered wooden boards"/>

    <!-- Brand -->
    <text class="condensed brand-name" x="414" y="150" font-size="74" textLength="354" lengthAdjust="spacingAndGlyphs">CORVALO</text>

    <!-- Frame -->
    <rect class="frame-line" x="30" y="186" width="1140" height="288"/>
    <line class="frame-line" x1="518" y1="186" x2="518" y2="474"/>
    <line class="frame-line" x1="518" y1="322" x2="1170" y2="322"/>

    <!-- Headline -->
    <text class="script" x="62" y="290" font-size="118">A</text>
    <text class="condensed" x="134" y="288" font-size="92" textLength="336" lengthAdjust="spacingAndGlyphs">UTHENTIC</text>
    <text class="condensed" x="70" y="452" font-size="170" textLength="406" lengthAdjust="spacingAndGlyphs">SPANISH</text>

    <!-- Offer -->
    <text class="condensed" x="554" y="284" font-size="74" textLength="584" lengthAdjust="spacingAndGlyphs">CAFE · DELI · TAPAS · BAR</text>

    <!-- Icons: coffee, bread, cheese, wine -->
    <g class="offer-icons">
      <g class="icon-coffee">
        <path class="icon-stroke" d="M580 352 q-6 -8 0 -16 q6 -8 0 -16"/>
        <path class="icon-stroke" d="M596 352 q-6 -8 0 -16 q6 -8 0 -16"/>
        <path class="icon-stroke" d="M612 352 q-6 -8 0 -16 q6 -8 0 -16"/>
        <path class="icon" d="M564 362 h86 v52 a22 22 0 0 1 -22 22 h-42 a22 22 0 0 1 -22 -22 z"/>
        <path class="icon-stroke" stroke-width="8" d="M650 378 h8 a12 12 0 0 1 0 24 h-8"/>
        <rect class="icon" x="560" y="440" width="96" height="8" rx="3"/>
      </g>
      <g class="icon-bread">
        <path class="icon" d="M718 400 q0 -20 24 -22 h56 q24 2 24 22 v34 q0 6 -6 6 h-92 q-6 0 -6 -6 z"/>
        <path class="icon-stroke" stroke="var(--roast-mid)" stroke-width="3" d="M748 384 v10 M770 384 v10 M792 384 v10"/>
      </g>
      <g class="icon-cheese">
        <path class="icon" d="M880 396 l44 -30 l72 18 v52 h-116 z"/>
        <path fill="var(--roast-mid)" d="M892 402 h96 v26 h-96 z"/>
        <circle cx="912" cy="414" r="5" class="icon"/>
        <circle cx="952" cy="420" r="4" class="icon"/>
      </g>
      <g class="icon-wine">
        <path class="icon-stroke" stroke-width="4" d="M1068 348 q-2 38 10 52 q10 10 20 10 q10 0 20 -10 q12 -14 10 -52"/>
        <path class="icon" d="M1072 374 q2 22 10 30 q8 6 16 6 q8 0 16 -6 q8 -8 10 -30 z"/>
        <rect class="icon" x="1095" y="408" width="6" height="34"/>
        <rect class="icon" x="1076" y="440" width="44" height="6" rx="3"/>
      </g>
    </g>

    <!-- Footer -->
    <text class="condensed" x="62" y="568" font-size="70" textLength="405" lengthAdjust="spacingAndGlyphs">COMING <tspan class="script" font-size="84">S</tspan>OON!</text>
    <text class="condensed" x="528" y="568" font-size="70" textLength="640" lengthAdjust="spacingAndGlyphs">WWW.CORVALOBAR.EXAMPLE.NZ</text>
  </svg>
</main>
</body>
</html>
```